Staff Newsletter Template Image

We are looking for two .jpg images that we can put into a Word document and use for our staff newsletter. We will then add content using text boxes.
Attached is the current template which works for the columns and size that we need but we just want a fresh new design.
The Word document shows how we use it.
The name will stay the same - Team upBeat but can be a different look to the current one.

Target Market(s)

Sales team

Colors

Designer to choose colors to be used in the design.

Requirements
Must have
• Colours will be green, grey and white, possibly cream if needed. All from the guidelines.
• I have attached our brand guidelines which shows design elements and fonts for our brand. Also attached is brand guidelines for one of our product lines as we would like to use the same green.
• It needs to be nice to look at and motivational for our team

```html
<!DOCTYPE html>
<html lang="en">
<head>
<meta charset="UTF-8">
<title>Team upBeat – Staff Newsletter</title>
<link rel="stylesheet" href="https://fonts.googleapis.com/css2?family=Josefin+Sans:wght@300&display=swap">
<style>
  :root {
    --leaf: #5f9a3c;
    --sage: #a9cb8c;
    --graphite: #3c3c3c;
    --paper: #ffffff;
    --mist: #eef1ec;
  }
  html, body {
    margin: 0;
    padding: 0;
    overflow: hidden;
    background: var(--paper);
  }
  .sheet {
    position: relative;
    width: 848px;
    height: 1200px;
    overflow: hidden;
    background: var(--paper);
    font-family: "Josefin Sans", sans-serif;
    font-weight: 300;
  }
  .sheet__bands {
    position: absolute;
    inset: 0;
  }
  .band--sage { fill: var(--sage); }
  .band--leaf { fill: var(--leaf); }
  .band--footer { fill: var(--graphite); }
  .masthead {
    position: absolute;
    left: 56px;
    top: 96px;
    margin: 0;
    font-size: 50px;
    font-weight: 300;
    letter-spacing: 1px;
    color: var(--graphite);
    line-height: 1;
    white-space: nowrap;
  }
  .backdrop-name {
    position: absolute;
    left: 0;
    width: 848px;
    top: 640px;
    margin: 0;
    padding-left: 110px;
    box-sizing: border-box;
    text-align: center;
    font-size: 96px;
    font-weight: 300;
    letter-spacing: 2px;
    color: var(--mist);
    line-height: 1;
    white-space: nowrap;
  }
</style>
</head>
<body>
  <main class="sheet">
    <svg class="sheet__bands" width="848" height="1200" viewBox="0 0 848 1200" aria-hidden="true">
      <polygon class="band--sage" points="342,23 522,0 848,0 848,158" />
      <polygon class="band--leaf" points="0,0 522,0 0,68" />
      <polygon class="band--leaf" points="324,1180 848,1111 848,1180" />
      <rect class="band--footer" x="0" y="1180" width="848" height="20" />
    </svg>

    <h1 class="masthead">Team upBeat</h1>

    <p class="backdrop-name" aria-hidden="true">Team upBeat</p>
  </main>
</body>
</html>
```